Business Card Design Project

A polished, very professional looking business card. I think we want to keep it all grey. I've attached our old logo, and current mockup in which case we really like the font.

Target Market(s)

Target Market are Bride and Grooms and Wedding Coordinators. We are wedding photographers

Industry/Entity Type

Business

Font styles to use
Serif
Sans Serif

Requirements
Must have
• An elegant, yet simple and sophisticated appearance.

Phone number, Email, Website and Social Media link.
Nice to have
• An element that can be spot glossed when printed. Not necessary though.
Should not have
• Bright colors, images or intensive graphics.

```html
<!DOCTYPE html>
<html lang="en">
<head>
<meta charset="utf-8">
<title>Colin Marsh Photographers – Business Card</title>
<link rel="stylesheet" href="https://fonts.googleapis.com/css2?family=Cormorant+SC:wght@500;600&family=Arimo:wght@400&display=swap">
<style>
  :root {
    --canvas: #e4e4e4;
    --charcoal: #4a4a4c;
    --card-white: #f7f7f8;
    --ink: #3d3d3f;
    --ink-soft: #5b5b5e;
    --ground-light: #e2e2e3;
    --ground-mid: #c4c4c6;
    --ground-dark: #8e8e91;
    --white: #ffffff;
    --serif: "Cormorant SC", "Times New Roman", serif;
    --sans: "Arimo", Arial, sans-serif;
  }
  * { box-sizing: border-box; margin: 0; padding: 0; }
  html, body { width: 1200px; height: 1200px; overflow: hidden; background: var(--canvas); }
  .canvas { position: relative; width: 1200px; height: 1200px; }

  .card {
    position: absolute; left: 180px; width: 840px; height: 480px;
    overflow: hidden; box-shadow: 0 6px 20px rgba(0,0,0,.18);
  }

  /* Back side */
  .card-back { top: 100px; background: var(--charcoal); color: var(--white); }
  .card-back .mark {
    position: absolute; left: 50%; top: 150px; width: 64px; height: 64px;
    margin-left: -32px; background: var(--white);
  }
  .card-back .rule {
    position: absolute; left: 50%; top: 232px; width: 22px; margin-left: -11px;
    border-top: 1px solid var(--white);
  }
  .card-back .brand-name {
    position: absolute; left: 0; right: 0; top: 248px; text-align: center;
    font-family: var(--serif); font-weight: 500; font-size: 30px; letter-spacing: 5px;
  }
  .card-back .brand-sub {
    position: absolute; left: 0; right: 0; top: 292px; text-align: center;
    font-family: var(--serif); font-weight: 600; font-size: 10px; letter-spacing: 7px;
  }

  /* Front side */
  .card-front { top: 620px; background: var(--card-white); }
  .ground {
    position: absolute; left: 0; right: 0; top: 285px; bottom: 0;
    background: linear-gradient(180deg, var(--ground-light) 0%, var(--ground-mid) 55%, #b2b2b4 100%);
  }
  .ground-band {
    position: absolute; left: 0; right: 0; bottom: 0; height: 80px;
    background: linear-gradient(180deg, #a6a6a8, #7e7e81);
  }
  .photographer-figure {
    position: absolute; left: 28px; top: 140px; width: 210px; height: 270px;
    background: linear-gradient(180deg, #3a3a3c 0%, #555557 70%, #7a7a7c 100%);
    border-radius: 4px;
  }
  .front-name {
    position: absolute; left: 250px; width: 420px; top: 34px; text-align: center;
    font-family: var(--serif); font-weight: 500; font-size: 36px; letter-spacing: 5px;
    color: var(--ink);
  }
  .front-sub {
    position: absolute; left: 250px; width: 420px; top: 82px; text-align: center;
    font-family: var(--serif); font-weight: 600; font-size: 11px; letter-spacing: 8px;
    color: var(--ink-soft);
  }
  .front-mark {
    position: absolute; left: 318px; top: 128px; width: 112px; height: 112px;
    background: var(--charcoal);
  }
  .front-mark-label {
    position: absolute; left: 300px; width: 148px; top: 248px; text-align: center;
    font-family: var(--serif); font-weight: 500; font-size: 15px; letter-spacing: 2px;
    color: var(--ink);
  }
  .divider {
    position: absolute; left: 470px; top: 118px; width: 1px; height: 180px;
    background: linear-gradient(180deg, transparent, var(--ink-soft) 30%, var(--ink-soft) 70%, transparent);
  }
  .contact-list { position: absolute; left: 496px; top: 138px; list-style: none; }
  .contact-list li {
    display: flex; align-items: center; height: 28px;
    font-family: var(--sans); font-size: 15px; color: var(--ink-soft);
  }
  .contact-list svg { width: 16px; height: 16px; margin-right: 14px; flex: none; }
  .tagline {
    position: absolute; left: 262px; top: 374px;
    font-family: var(--serif); font-weight: 500; font-size: 17px; letter-spacing: 1.5px;
    color: var(--white); white-space: nowrap;
  }
</style>
</head>
<body>
<main class="canvas">

  <section class="card card-back" aria-label="Business card, back">
    <div class="mark"></div>
    <div class="rule"></div>
    <h1 class="brand-name">Colin Marsh</h1>
    <p class="brand-sub">PHOTOGRAPHERS</p>
  </section>

  <section class="card card-front" aria-label="Business card, front">
    <div class="ground"></div>
    <div class="ground-band"></div>
    <div class="photographer-figure" role="img" aria-label="Silhouette of a photographer leaning over a camera on a tripod"></div>

    <h2 class="front-name">Colin Marsh</h2>
    <p class="front-sub">PHOTOGRAPHERS</p>

    <div class="front-mark"></div>
    <p class="front-mark-label">Colin Marsh</p>

    <div class="divider"></div>

    <ul class="contact-list">
      <li>
        <svg viewBox="0 0 16 16" aria-hidden="true"><circle cx="8" cy="8" r="7" fill="none" stroke="#6a6a6d"/><path d="M5.5 4.5l1.5 0 .6 2-1 .8a5 5 0 0 0 2.1 2.1l.8-1 2 .6v1.5a1 1 0 0 1-1 1A6 6 0 0 1 4.5 5.5a1 1 0 0 1 1-1z" fill="#6a6a6d"/></svg>
        555.010.2468
      </li>
      <li>
        <svg viewBox="0 0 16 16" aria-hidden="true"><circle cx="8" cy="8" r="7" fill="none" stroke="#6a6a6d"/><circle cx="8" cy="8" r="3" fill="#6a6a6d"/></svg>
        photobook.net/ColinMarshPhoto
      </li>
      <li>
        <svg viewBox="0 0 16 16" aria-hidden="true"><circle cx="8" cy="8" r="7" fill="none" stroke="#6a6a6d"/><circle cx="8" cy="8" r="3" fill="#6a6a6d"/></svg>
        chirp.net/ColinMarsh
      </li>
      <li>
        <svg viewBox="0 0 16 16" aria-hidden="true"><circle cx="8" cy="8" r="7" fill="none" stroke="#6a6a6d"/><rect x="4.5" y="5.5" width="7" height="5" fill="none" stroke="#6a6a6d"/><path d="M4.5 5.5L8 8.5l3.5-3" fill="none" stroke="#6a6a6d"/></svg>
        colin@colinmarshstudio.com
      </li>
      <li>
        <svg viewBox="0 0 16 16" aria-hidden="true"><circle cx="8" cy="8" r="7" fill="none" stroke="#6a6a6d"/><circle cx="8" cy="8" r="3.5" fill="none" stroke="#6a6a6d"/><path d="M4.5 8h7M8 4.5v7" stroke="#6a6a6d"/></svg>
        www.colinmarshstudio.com
      </li>
    </ul>

    <p class="tagline">California based wedding and portrait photographer</p>
  </section>

</main>
</body>
</html>
```